5x5 Pop Up Display, Company Logo With Text and Graphics for Tradeshow Display

Design for a 5ft x 5ft pop up trade show display that will sit on top of a table. I usually prefer clean, somewhat minimalist designs. We are a food service company but it's not a requirement to have photos of food. Design elements should compliment the table cloth that we have for the booth. The below may be included depending on the design aesthetic.
Service Provided: Daily Meal Service, Kitchen Management
"Nationwide Footprint"
"Grassroots Service"
"Fresh Scratch Cooking"
"Custom Menus"
"Made To Order Meals"

```html
<!DOCTYPE html>
<html lang="en">
<head>
<meta charset="utf-8">
<title>Hale Hearth – Tradeshow Display</title>
<link rel="stylesheet" href="https://fonts.googleapis.com/css2?family=Old+Standard+TT:ital,wght@0,400;0,700;1,400&display=swap">
<style>
  :root {
    --bg-light: #e1e3dc;
    --bg-center: #e4e6e0;
    --sage-1: #c9d1c1;
    --sage-2: #b7c3ad;
    --sage-3: #a9b79e;
    --ink: #0d0d0d;
    --ink-soft: #2a2a2a;
    --accent: #7fb241;
  }
  * { margin: 0; padding: 0; box-sizing: border-box; }
  html, body { width: 1200px; height: 1200px; overflow: hidden; }
  body { background: var(--bg-light); }
  .display {
    position: relative;
    width: 1200px;
    height: 1200px;
    overflow: hidden;
    font-family: "Old Standard TT", Georgia, serif;
  }
  .backdrop { position: absolute; inset: 0; }
  .content {
    position: absolute;
    inset: 0;
    text-align: center;
  }
  .brand {
    position: absolute;
    top: 70px;
    left: 0;
    right: 0;
    color: var(--ink);
    font-weight: 700;
    font-variant: small-caps;
    font-size: 188px;
    line-height: 158px;
    letter-spacing: -2px;
  }
  .brand-line { display: block; }
  .brand-mark {
    display: inline-block;
    width: 64px;
    height: 64px;
    border-radius: 50%;
    background: var(--accent);
    margin-left: 18px;
    vertical-align: 12px;
  }
  .services {
    position: absolute;
    top: 472px;
    left: 0;
    right: 0;
    color: var(--ink-soft);
    font-weight: 700;
    font-size: 80px;
    line-height: 94px;
    letter-spacing: 0.5px;
  }
  .highlights {
    position: absolute;
    top: 710px;
    left: 0;
    right: 0;
    list-style: none;
    color: var(--ink-soft);
    font-style: italic;
    font-size: 70px;
    line-height: 84px;
    letter-spacing: 1px;
  }
</style>
</head>
<body>
<main class="display">
  <svg class="backdrop" width="1200" height="1200" viewBox="0 0 1200 1200" aria-hidden="true">
    <defs>
      <radialGradient id="center-glow" cx="0.58" cy="0.45" r="0.6">
        <stop offset="0" stop-color="#e6e8e2"/>
        <stop offset="0.7" stop-color="#dcdfd7"/>
        <stop offset="1" stop-color="#c7cfbf"/>
      </radialGradient>
      <linearGradient id="wave-left" x1="0" y1="0" x2="1" y2="1">
        <stop offset="0" stop-color="#c3ccba"/>
        <stop offset="1" stop-color="#aebba3"/>
      </linearGradient>
      <linearGradient id="wave-right" x1="1" y1="0" x2="0" y2="1">
        <stop offset="0" stop-color="#d3d9cc"/>
        <stop offset="1" stop-color="#b3bfa8"/>
      </linearGradient>
    </defs>
    <rect width="1200" height="1200" fill="url(#center-glow)"/>
    <path d="M0 300 C 200 330, 330 470, 420 640 C 500 800, 600 1000, 900 1200 L 0 1200 Z" fill="url(#wave-left)" opacity="0.75"/>
    <path d="M0 560 C 200 560, 330 700, 420 860 C 500 1000, 560 1120, 700 1200 L 0 1200 Z" fill="#b4c0aa" opacity="0.6"/>
    <path d="M0 900 C 160 880, 320 980, 420 1200 L 0 1200 Z" fill="#a9b79e" opacity="0.55"/>
    <path d="M900 0 C 1080 80, 1160 300, 1110 560 C 1070 780, 980 960, 820 1200 L 1200 1200 L 1200 0 Z" fill="url(#wave-right)" opacity="0.7"/>
    <path d="M1200 420 C 1120 700, 1040 960, 1000 1200 L 1200 1200 Z" fill="#b7c3ad" opacity="0.55"/>
    <path d="M0 1080 C 300 1020, 700 1060, 1200 1150 L 1200 1200 L 0 1200 Z" fill="#c9d1c1" opacity="0.5"/>
  </svg>

  <section class="content">
    <h1 class="brand">
      <span class="brand-line">Hale<span class="brand-mark"></span></span>
      <span class="brand-line">Hearth</span>
    </h1>
    <h2 class="services">Daily Meal Service<br>Kitchen Management</h2>
    <ul class="highlights">
      <li>Nationwide Footprint</li>
      <li>Grassroots Service</li>
      <li>Fresh Scratch Cooking</li>
      <li>Custom Menus</li>
      <li>Made To Order Meals</li>
    </ul>
  </section>
</main>
</body>
</html>
```